Bright Harbor Dental*

Promotion for a new dental office
brightharbrdntl.example

I just opened a new dental office and would like to promote my office to
the public. I attached some examples. I have AI files for logo and also can
provide office pictures. Website is brightharbordntl.example.

Target Market(s)

General public

Requirements
Must have
• Dr. Olund
• Kessler State U, BS, MCB
• Marrow Vale School of Dentistry
• Grenfield Guard veteran
• New patient exam, X-rays and basic cleaning for $95.
• White background
• 20% discount with this post card. This only applied to private pay patients(in fine print)
• Open saturdays and evenings
Should not have
• No postal info. Not going to mail this out.

```html
<!DOCTYPE html>
<html lang="en">
<head>
<meta charset="utf-8">
<title>Bright Harbor Dental – Postcard</title>
<link href="https://fonts.googleapis.com/css2?family=Montserrat:wght@300;400;500;600;700;800&family=Oswald:wght@400;500&family=Great+Vibes&display=swap" rel="stylesheet">
<style>
  :root{
    --page:#e6e7e9;
    --paper:#ffffff;
    --teal:#1b9cc6;
    --teal-deep:#17839f;
    --ink:#2f2f31;
    --ink-band:#3b3a3d;
    --grey-arc:#a9abae;
    --line:#d5d7da;
    --muted:#6d6e71;
  }
  *{margin:0;padding:0;box-sizing:border-box}
  html,body{width:897px;height:1200px;overflow:hidden;background:var(--page)}
  body{position:relative;font-family:"Montserrat",sans-serif;color:var(--ink)}

  .card{position:absolute;left:60px;width:770px;height:513px;background:var(--paper);overflow:hidden}
  .card--front{top:42px}
  .card--back{top:616px}
  .card__art{position:absolute;inset:0;width:770px;height:513px}

  .brand{position:absolute;left:30px;top:20px;display:flex;align-items:center;gap:12px}
  .brand__mark{width:68px;height:68px;border:1.5px solid #58595b;border-radius:50%;flex:none}
  .brand__name{font-weight:300;font-size:19px;letter-spacing:.5px;color:#4a4b4d;line-height:1;white-space:nowrap}
  .brand__tag{font-size:10px;font-weight:500;letter-spacing:.3px;color:var(--ink);margin-top:8px;padding-left:22px}

  .headline{position:absolute;left:34px;top:116px;font-size:41px;line-height:44px;text-transform:uppercase}
  .headline .accent{color:var(--teal-deep);font-weight:800}
  .headline .plain{font-weight:400}
  .headline .strong{font-weight:800}

  .script{position:absolute;left:26px;top:300px;width:280px;height:60px;font-family:"Great Vibes",cursive;color:var(--teal);font-size:24px;line-height:26px}
  .script__line2{padding-left:46px}
  .script__smile{font-size:40px;color:var(--ink);position:absolute;left:150px;top:10px;white-space:nowrap;line-height:1}

  .touch{position:absolute;left:22px;top:384px;color:#fff;font-size:16px;font-weight:400;letter-spacing:.3px}
  .touch b{color:var(--teal);font-weight:800}

  .contact{position:absolute;left:24px}
  .contact__call{font-family:"Oswald",sans-serif;font-size:33px;line-height:1;color:#fff;white-space:nowrap;transform:scaleX(.86);transform-origin:left}
  .contact__call .num{font-weight:500}
  .contact__lang{font-size:15.5px;color:#fff;margin-top:8px;letter-spacing:.2px}
  .contact__web{font-size:12.5px;color:#fff;margin-top:8px;letter-spacing:.2px}
  .card--front .contact{top:422px}
  .card--back .contact{top:424px}
  .card--back .contact__call .lead{color:var(--teal)}
  .card--back .contact__web{color:var(--teal)}

  .care{position:absolute;right:442px;top:128px;text-align:right;font-size:31px;line-height:37px;font-weight:800;text-transform:uppercase;color:#3a393c}
  .care .accent{color:var(--teal)}

  .offer{position:absolute;left:25px;top:300px;font-size:19px;line-height:24px;font-weight:500;color:var(--ink)}
  .offer b{font-weight:800}
  .price{position:absolute;left:292px;top:300px;width:118px;height:48px;background:var(--ink);clip-path:polygon(12% 0,100% 0,88% 100%,0 100%);color:#fff;font-weight:800;font-size:38px;line-height:48px;text-align:center}
  .price sup{font-size:20px;vertical-align:top;line-height:30px}

  .perks{position:absolute;left:22px;top:372px;color:#fff;font-weight:700;font-size:15px;line-height:23px;letter-spacing:.2px}

  .doctor{position:absolute;left:520px;top:40px;width:222px}
  .doctor__label{font-size:12px;font-weight:700;letter-spacing:1px;color:var(--teal)}
  .doctor__name{font-size:34px;font-weight:800;color:var(--ink);line-height:1.1;margin-top:6px}
  .doctor__rule{width:60px;height:3px;background:var(--teal);margin:12px 0 14px}
  .doctor__facts{list-style:none;font-size:13px;line-height:19px;font-weight:500;color:var(--ink)}
  .doctor__facts li{padding-left:16px;position:relative;margin-bottom:8px}
  .doctor__facts li::before{content:"";position:absolute;left:0;top:6px;width:7px;height:7px;border-radius:50%;background:var(--teal)}

  .discount{position:absolute;left:520px;top:300px;width:222px;border:2px solid var(--teal);padding:12px 14px;text-align:center}
  .discount__value{font-size:40px;font-weight:800;color:var(--teal);line-height:1}
  .discount__value span{font-size:22px;color:var(--ink)}
  .discount__note{font-size:13px;font-weight:600;color:var(--ink);margin-top:6px;letter-spacing:.3px;text-transform:uppercase}
  .fine-print{position:absolute;left:520px;top:418px;width:222px;font-size:9.5px;line-height:13px;color:var(--muted)}
</style>
</head>
<body>

<section class="card card--front">
  <svg class="card__art" viewBox="0 0 770 513">
    <defs>
      <linearGradient id="familyTones" x1="0" y1="0" x2="1" y2="1">
        <stop offset="0" stop-color="#d9b24a"/>
        <stop offset=".35" stop-color="#e8cfae"/>
        <stop offset=".65" stop-color="#efe6d6"/>
        <stop offset="1" stop-color="#6f8a3e"/>
      </linearGradient>
      <clipPath id="lowerHalf"><rect x="0" y="262" width="770" height="300"/></clipPath>
    </defs>
    <rect x="0" y="402" width="560" height="111" fill="#1b9cc6"/>
    <path d="M0 382 H184 L170 402 H0 Z" fill="#3b3a3d"/>
    <circle cx="660" cy="262" r="342" fill="#a9abae"/>
    <circle cx="660" cy="262" r="342" fill="#1b9cc6" clip-path="url(#lowerHalf)"/>
    <circle cx="660" cy="262" r="326" fill="#ffffff"/>
    <circle cx="660" cy="262" r="316" fill="url(#familyTones)" role="img" aria-label="Photo of a smiling multi-generation family outdoors in autumn"/>
    <path d="M212 360 Q238 382 270 372 Q290 364 294 346" fill="none" stroke="#1b9cc6" stroke-width="2.5"/>
    <path d="M287 348 L296 342 L300 353" fill="none" stroke="#1b9cc6" stroke-width="2"/>
  </svg>

  <div class="brand">
    <span class="brand__mark"></span>
    <div>
      <div class="brand__name">BRIGHT HARBOR DENTAL</div>
      <div class="brand__tag">MODERN GENERAL DENTISTRY</div>
    </div>
  </div>

  <h1 class="headline">
    <span class="accent">Patient</span><br>
    <span class="accent">Comfort</span><br>
    <span class="plain">Is our top</span><br>
    <span class="strong">Priority</span>
  </h1>

  <p class="script">
    Let us help you keep<br>
    <span class="script__line2">that beautiful</span>
    <span class="script__smile">Smile!</span>
  </p>

  <p class="touch">GET <b>IN TOUCH</b></p>

  <div class="contact">
    <div class="contact__call"><span class="lead">CALL TODAY!</span> <span class="num">555-014-2290</span></div>
    <div class="contact__lang">SE HABLA ESPAÑOL</div>
    <div class="contact__web">WWW.BRIGHTHARBORDNTL.EXAMPLE</div>
  </div>
</section>

<section class="card card--back">
  <svg class="card__art" viewBox="0 0 770 513">
    <defs>
      <radialGradient id="clinicTones" cx=".75" cy=".5" r=".7">
        <stop offset="0" stop-color="#ffffff"/>
        <stop offset=".5" stop-color="#f1f3f3"/>
        <stop offset="1" stop-color="#e3e8e6"/>
      </radialGradient>
      <clipPath id="upperArc"><rect x="0" y="0" width="770" height="256"/></clipPath>
      <clipPath id="innerPanel"><circle cx="44" cy="256" r="420"/></clipPath>
    </defs>
    <circle cx="44" cy="256" r="442" fill="#a9abae"/>
    <circle cx="44" cy="256" r="442" fill="#1b9cc6" clip-path="url(#upperArc)"/>
    <circle cx="44" cy="256" r="428" fill="#ffffff"/>
    <circle cx="44" cy="256" r="420" fill="url(#clinicTones)" role="img" aria-label="Soft photo of a tooth model and dental mirror"/>
    <g clip-path="url(#innerPanel)">
      <rect x="0" y="368" width="770" height="50" fill="#1b9cc6"/>
      <rect x="0" y="418" width="770" height="95" fill="#3b3a3d"/>
    </g>
  </svg>

  <div class="brand">
    <span class="brand__mark"></span>
    <div>
      <div class="brand__name">BRIGHT HARBOR DENTAL</div>
      <div class="brand__tag">MODERN GENERAL DENTISTRY</div>
    </div>
  </div>

  <h2 class="care">
    Personal care<br>
    <span class="accent">Quality care</span><br>
    Patient care<br>
    <span class="accent">Modern care</span>
  </h2>

  <p class="offer">New Patient Exam, X-rays<br>and <b>Basic Cleaning</b> for</p>
  <div class="price"><sup>$</sup>95</div>

  <p class="perks">OPEN EVENINGS AND SATURDAYS<br>MODERN STATE OF THE ART EQUIPMENT</p>

  <div class="contact">
    <div class="contact__call"><span class="lead">CALL TODAY!</span> <span class="num">555-014-2290</span></div>
    <div class="contact__lang">SE HABLA ESPAÑOL</div>
    <div class="contact__web">WWW.BRIGHTHARBORDNTL.EXAMPLE</div>
  </div>

  <div class="doctor">
    <p class="doctor__label">MEET YOUR DENTIST</p>
    <p class="doctor__name">Dr. Olund</p>
    <div class="doctor__rule"></div>
    <ul class="doctor__facts">
      <li>Kessler State U, BS, MCB</li>
      <li>Marrow Vale School of Dentistry</li>
      <li>Grenfield Guard Veteran</li>
      <li>Open Evenings &amp; Saturdays</li>
    </ul>
  </div>

  <div class="discount">
    <p class="discount__value">20% <span>OFF*</span></p>
    <p class="discount__note">with this postcard</p>
  </div>
  <p class="fine-print">*Discount applies only to private pay patients. Cannot be combined with other offers.</p>
</section>

</body>
</html>
```